Energy Supplement Company Needs Packaging Design! See Your Design In Stores Everywhere!

Have you ever dreamed of seeing your designs on store shelves, billboards and in the hands of celebrities and professional athletes?

Well, your dreams may just come true… You now have the chance to have your design on the product packaging of the next major energy supplement company!

BRISKLO Vigor, Inc. is inviting the most creative, ambitious and talented designers to create a new look and feel for our brand's most popular products, the BRISKLO Vigor Tablets.

BRISKLO Vigor, Inc. began in 1985 by creating the original energy tablet, most recognized for its iconic blue packet featured in over 20,000 retail stores today. The company grew through their grass roots philosophy of distribution and quickly expanded across the United States through dozens of regional and national chains like 4-22, Marlow Q and PVD. In February of 2001, the founder of BriskLo passed and the company’s grass roots approach lost momentum and distribution as the fierce competition from energy shots and drinks hit the space that they once owned.

Theodore Lasko, a 26 year user of BRISKLO tablets, noticed that his favorite daily energy product was becoming increasingly more difficult to find in stores. As an active, serial entrepreneur with numerous ventures, his deep passion for BRISKLO led him to explore the opportunity to get involved with the company (get involved is an understatement). On August 1st of 2012, Theo raised capital and bought the company.

To increase awareness and spread his passion for BRISKLO, Mr. Lasko organized and structured the new BRISKLO Vigor, Inc. by bringing on a talented Team and investors, including Rex Palmore, a renowned sports agent/owner of the largest basketball agency whose clients include some of the biggest names in the sport. The amazing quality of our products coupled with the loyal following from the masses has led the brand to new heights and sponsorship opportunities with major sports teams and athletic organizations.

Now that the future is looking UP, we are looking for a brand refresh to bring our tablets current.

Your mission -should you chose to accept- is to develop a new graphic design for our energy tablet packets. We expect the graphic design to be modern, sleek and appealing to an 18-34 demographic. This new design will serve as the vehicle to spark excitement about energy tablets and their superiority over other forms of energy supplements. However, most importantly, you must make the package eye catching yet trusting and approachable. Keep in mind that this is something you would see in a retail store and feel comfortable reaching for and trying.

It is important to stress the mainstream direction of our company. The current packaging is somewhat 'dated' and may be out of touch with mainstream interests. Just like your aunt still rocking shoulder pads and leg warmers, we need to leave the 1980s and join everyone in 2013. Although we will begin positioning our brand towards mainstream sports, our goal is to have our products everywhere from the sidelines of major sporting events to board meetings of fortune 500 companies to the backpacks of college students. Therefore, the winning design will be one that transcends the interests of a specific group and appeals to the broader audience. Remember this is something you could see Darnell Voss, Otto Frame, and your mother holding.

Here's the great part: We are leaving all of the designing up to you!

You can redesign everything and anything you want (change colors, company logo design, content, etc.). Think of it as a blank canvas.

If you have any questions regarding design or BRISKLO Vigor, Inc. in general, please feel free to email us at design@brisk-lo.example or check out our website at www.brisk-lo.example.

Good luck!

Hi Everyone! 

Thank you to everyone who has submitted designs! Seeing what you all have come up with is exciting and impressive. However, we want to address a few commonly asked questions as well as a few general comments we have overall. 

To start, we'll better explain what we want to see in the designs. 

Although we are an energy company, we are looking to be very contemporary and sleek. Our current brand and packaging is bright and colorful, but that doesn't necessarily fit with the repositioning of our brand as a mainstream energy brand. Designs should try to only include a few colors at most. Each tablet packet should look great one their own and amazing together. 

Moreover, the designs should be relatively minimalistic. We aren't looking for anything to be "in your face". We need to reintroduce to the 18-34 generation that taking energy tablets are safe, effective, and a superior way of consuming energy supplements. Therefore, an approachable packet design is imperative. Neon colors, electricity, etc. only makes the product look scary and intimidating. 

To sum up:
Ø Use only a few colors
Ø Target an 18-34 year old demographic
Ø Minimalistic/approachable design
Ø Move away from Retro look with bright colors

FAQs:
1) We have been asked about whether or not you should be redesigning the logo on the packaging also. The answer is YES. We want every part of the packets updated. You are also designing 3 different packets or our whole energy tablet line (Surge Mix, Summit Mix, and Botanic Mix). 

2) The packets have a height of 4'' and a width of 3''. They are double-sided, so if you have a creative way of designing the back panel with the supplement facts, we would love to see it. 

We want all of you to know that we appreciate all of your hard work on creating these designs and helping to rebrand our company. Again, if you have any questions at all, the best way to reach us is by emailing us at design@brisk-lo.example. 

THANK YOU!!

The BRISKLO Design Team

Reason: We are extending the deadline for designs until Friday April 26th. We hope this will give designers a chance to submit final designs for the competition. As always, please feel free to email us directly at design@brisk-lo.example if you have any questions.

Hi everyone!

Just to let you all know, the design contest ends at 1:37am on Saturday, April 27th. We didn't want to mislead any of you by saying the contest ends tomorrow since you only have an hour and a half to submit any designs after 12am tonight. Therefore, we suggest you submit any designs you want considered by tonight. 

Thanks and good luck! 

The BRISKLO Design Team

Target Market(s)

18-34 year olds. Active, mainstream audience (not extreme-sports fans)

Requirements
Must have
• Product packet is 4''x3''
Should not have
• -Pictures of sports equipment.
-Resemble other energy products
-Look scary or intimidating
-Should not look like a cartoon or animation
-No neon colors

```html
<!DOCTYPE html>
<html lang="en">
<head>
<meta charset="utf-8">
<title>BRISKLO Vigor Tablets – Packet Line</title>
<link href="https://fonts.googleapis.com/css2?family=Arimo:ital,wght@0,400;0,700;1,700&family=Roboto+Condensed:wght@400;700&display=swap" rel="stylesheet">
<style>
  :root {
    --canvas: #ffffff;
    --ink: #0d0d0d;
    --white: #ffffff;
    --yellow: #f2ee1f;
    --green: #4fb81a;
    --green-light: #9be03a;
    --green-text: #86c923;
    --blue: #0f5fc4;
    --blue-light: #5fc8f2;
    --blue-text: #49c2ee;
    --silver: #8e8f91;
    --silver-light: #e4e5e6;
  }
  * { margin: 0; padding: 0; box-sizing: border-box; }
  html, body { width: 1200px; height: 900px; overflow: hidden; background: var(--canvas); }
  body { position: relative; font-family: "Arimo", Arial, sans-serif; }

  .packet {
    position: absolute;
    width: 320px;
    height: 506px;
    overflow: hidden;
    background: linear-gradient(135deg, var(--tone-light) 0%, var(--tone) 45%, var(--tone-light) 100%);
    color: var(--white);
    transform-origin: top left;
  }
  .packet--botanic { --tone: var(--green); --tone-light: var(--green-light); --title: var(--yellow); --list: var(--green-text); --logo: var(--yellow); }
  .packet--surge   { --tone: var(--blue);  --tone-light: var(--blue-light);  --title: var(--blue-text); --list: var(--white); --logo: var(--blue-text); }
  .packet--summit  { --tone: var(--silver); --tone-light: var(--silver-light); --title: var(--yellow); --list: var(--white); --logo: var(--yellow); }

  .packet--large.packet--botanic { left: 47px; top: 38px; }
  .packet--large.packet--surge   { left: 430px; top: 38px; width: 333px; }
  .packet--large.packet--summit  { left: 800px; top: 38px; width: 336px; }
  .packet--small { transform: scale(0.6); }
  .packet--small.packet--botanic { left: 245px; top: 578px; }
  .packet--small.packet--surge   { left: 505px; top: 578px; }
  .packet--small.packet--summit  { left: 765px; top: 578px; }

  .packet__ground { position: absolute; inset: 0; width: 100%; height: 100%; }
  .packet__panel { fill: var(--ink); }
  .packet__swoosh { fill: none; stroke: var(--tone-light); stroke-width: 3; }

  .packet__trust { position: absolute; left: 14px; top: 14px; font-size: 7px; line-height: 1.1; color: var(--white); text-transform: uppercase; }
  .packet__trust-years { display: block; font-family: "Roboto Condensed", sans-serif; font-size: 22px; color: var(--yellow); line-height: 1; }
  .packet__trust-years small { font-size: 9px; color: var(--white); }

  .packet__tagline {
    position: absolute; left: 22px; top: 72px;
    font-family: "Roboto Condensed", sans-serif; font-size: 20px; letter-spacing: 0.5px;
    transform: rotate(-12deg); transform-origin: left center; white-space: nowrap;
  }
  .packet__tagline-star { color: var(--yellow); }

  .packet__brand { position: absolute; left: 30px; top: 155px; display: flex; align-items: center; gap: 10px; }
  .packet__brand-name { font-size: 52px; font-weight: 700; color: var(--logo); letter-spacing: 1px; }
  .packet__brand-dot { width: 18px; height: 18px; border-radius: 50%; background: var(--logo); }
  .packet__est { position: absolute; right: 26px; top: 222px; font-size: 11px; font-family: "Roboto Condensed", sans-serif; }

  .packet__formula { position: absolute; left: 30px; top: 300px; transform: rotate(-7deg); transform-origin: left top; white-space: nowrap; }
  .packet__ingredients { font-size: 17px; color: var(--list); font-family: "Roboto Condensed", sans-serif; }
  .packet--surge .packet__ingredients,
  .packet--summit .packet__ingredients { color: var(--white); }
  .packet__name { font-size: 29px; font-weight: 700; color: var(--title); line-height: 1.05; }
  .packet__extras { font-size: 15px; color: var(--list); line-height: 1.15; font-family: "Roboto Condensed", sans-serif; }

  .packet__count { position: absolute; right: 22px; top: 418px; text-align: right; font-size: 11px; line-height: 1.3; font-family: "Roboto Condensed", sans-serif; }
  .packet__facts { position: absolute; right: 18px; top: 446px; display: flex; gap: 5px; list-style: none; }
  .packet__fact { width: 29px; height: 15px; border: 1px solid var(--white); border-radius: 8px; font-size: 4px; text-align: center; line-height: 1.1; padding-top: 1px; text-transform: uppercase; }
  .packet__fact b { display: block; font-size: 6px; }
  .packet__label { position: absolute; right: 24px; bottom: 18px; font-size: 13px; font-family: "Roboto Condensed", sans-serif; text-transform: uppercase; }
</style>
</head>
<body>

<!-- Large row -->
<article class="packet packet--large packet--botanic">
  <svg class="packet__ground" viewBox="0 0 320 506" preserveAspectRatio="none" aria-hidden="true">
    <path class="packet__panel" d="M0 118 C90 55 210 40 320 48 L320 402 C220 428 110 455 0 478 Z"/>
    <path class="packet__swoosh" d="M0 486 C110 462 220 436 320 410"/>
  </svg>
  <p class="packet__trust">Trusted for over<span class="packet__trust-years">25 <small>years</small></span>Original</p>
  <p class="packet__tagline">FAST<span class="packet__tagline-star">★</span>BALANCED<span class="packet__tagline-star">★</span>LASTING</p>
  <div class="packet__brand"><span class="packet__brand-name">BRISKLO</span><span class="packet__brand-dot"></span></div>
  <p class="packet__est">EST.1985</p>
  <div class="packet__formula">
    <p class="packet__ingredients">GINSENG - GREEN TEA - ANGELICA</p>
    <h2 class="packet__name">BOTANIC MIX</h2>
    <p class="packet__extras">VITAMINS, MINERALS<br>ELEUTHERO, CAYENNE<br>SCISANDRA</p>
  </div>
  <p class="packet__count">USA<br>3 TABLETS</p>
  <ul class="packet__facts"><li class="packet__fact">Calories<b>0</b></li><li class="packet__fact">Sugar<b>0</b></li><li class="packet__fact">Gluten<b>0</b></li></ul>
  <p class="packet__label">Dietary Supplement</p>
</article>

<article class="packet packet--large packet--surge">
  <svg class="packet__ground" viewBox="0 0 320 506" preserveAspectRatio="none" aria-hidden="true">
    <path class="packet__panel" d="M0 118 C90 55 210 40 320 48 L320 402 C220 428 110 455 0 478 Z"/>
    <path class="packet__swoosh" d="M0 486 C110 462 220 436 320 410"/>
  </svg>
  <p class="packet__trust">Trusted for over<span class="packet__trust-years">25 <small>years</small></span>Original</p>
  <p class="packet__tagline">FAST<span class="packet__tagline-star">★</span>BALANCED<span class="packet__tagline-star">★</span>LASTING</p>
  <div class="packet__brand"><span class="packet__brand-name">BRISKLO</span><span class="packet__brand-dot"></span></div>
  <p class="packet__est">EST.1985</p>
  <div class="packet__formula">
    <p class="packet__ingredients">CoQ10 - GINSENG - GIMKO</p>
    <h2 class="packet__name">SURGE MIX</h2>
    <p class="packet__extras">MINERAL, AMINO ACIDS<br>ENZYMES, B-VITAMIN<br>ANTIOXIDANTS</p>
  </div>
  <p class="packet__count">USA<br>3 TABLETS</p>
  <ul class="packet__facts"><li class="packet__fact">Calories<b>0</b></li><li class="packet__fact">Sugar<b>0</b></li><li class="packet__fact">Gluten<b>0</b></li></ul>
  <p class="packet__label">Dietary Supplement</p>
</article>

<article class="packet packet--large packet--summit">
  <svg class="packet__ground" viewBox="0 0 320 506" preserveAspectRatio="none" aria-hidden="true">
    <path class="packet__panel" d="M0 118 C90 55 210 40 320 48 L320 402 C220 428 110 455 0 478 Z"/>
    <path class="packet__swoosh" d="M0 486 C110 462 220 436 320 410"/>
  </svg>
  <p class="packet__trust">Trusted for over<span class="packet__trust-years">25 <small>years</small></span>Original</p>
  <p class="packet__tagline">FAST<span class="packet__tagline-star">★</span>BALANCED<span class="packet__tagline-star">★</span>LASTING</p>
  <div class="packet__brand"><span class="packet__brand-name">BRISKLO</span><span class="packet__brand-dot"></span></div>
  <p class="packet__est">EST.1985</p>
  <div class="packet__formula">
    <p class="packet__ingredients">5-HTP-CoQ10-ROYAL JELLY</p>
    <h2 class="packet__name">SUMMIT MIX</h2>
    <p class="packet__extras">VITAMINS, MINERALS<br>ELEUTHERO, CAYENNE<br>SCISANDRA</p>
  </div>
  <p class="packet__count">USA<br>3 TABLETS</p>
  <ul class="packet__facts"><li class="packet__fact">Calories<b>0</b></li><li class="packet__fact">Sugar<b>0</b></li><li class="packet__fact">Gluten<b>0</b></li></ul>
  <p class="packet__label">Dietary Supplement</p>
</article>

<!-- Small row -->
<article class="packet packet--small packet--botanic">
  <svg class="packet__ground" viewBox="0 0 320 506" preserveAspectRatio="none" aria-hidden="true">
    <path class="packet__panel" d="M0 118 C90 55 210 40 320 48 L320 402 C220 428 110 455 0 478 Z"/>
    <path class="packet__swoosh" d="M0 486 C110 462 220 436 320 410"/>
  </svg>
  <p class="packet__trust">Trusted for over<span class="packet__trust-years">25 <small>years</small></span>Original</p>
  <p class="packet__tagline">FAST<span class="packet__tagline-star">★</span>BALANCED<span class="packet__tagline-star">★</span>LASTING</p>
  <div class="packet__brand"><span class="packet__brand-name">BRISKLO</span><span class="packet__brand-dot"></span></div>
  <p class="packet__est">EST.1985</p>
  <div class="packet__formula">
    <p class="packet__ingredients">GINSENG - GREEN TEA - ANGELICA</p>
    <h2 class="packet__name">BOTANIC MIX</h2>
    <p class="packet__extras">VITAMINS, MINERALS<br>ELEUTHERO, CAYENNE<br>SCISANDRA</p>
  </div>
  <p class="packet__count">USA<br>3 TABLETS</p>
  <ul class="packet__facts"><li class="packet__fact">Calories<b>0</b></li><li class="packet__fact">Sugar<b>0</b></li><li class="packet__fact">Gluten<b>0</b></li></ul>
  <p class="packet__label">Dietary Supplement</p>
</article>

<article class="packet packet--small packet--surge">
  <svg class="packet__ground" viewBox="0 0 320 506" preserveAspectRatio="none" aria-hidden="true">
    <path class="packet__panel" d="M0 118 C90 55 210 40 320 48 L320 402 C220 428 110 455 0 478 Z"/>
    <path class="packet__swoosh" d="M0 486 C110 462 220 436 320 410"/>
  </svg>
  <p class="packet__trust">Trusted for over<span class="packet__trust-years">25 <small>years</small></span>Original</p>
  <p class="packet__tagline">FAST<span class="packet__tagline-star">★</span>BALANCED<span class="packet__tagline-star">★</span>LASTING</p>
  <div class="packet__brand"><span class="packet__brand-name">BRISKLO</span><span class="packet__brand-dot"></span></div>
  <p class="packet__est">EST.1985</p>
  <div class="packet__formula">
    <p class="packet__ingredients">CoQ10 - GINSENG - GIMKO</p>
    <h2 class="packet__name">SURGE MIX</h2>
    <p class="packet__extras">MINERAL, AMINO ACIDS<br>ENZYMES, B-VITAMIN<br>ANTIOXIDANTS</p>
  </div>
  <p class="packet__count">USA<br>3 TABLETS</p>
  <ul class="packet__facts"><li class="packet__fact">Calories<b>0</b></li><li class="packet__fact">Sugar<b>0</b></li><li class="packet__fact">Gluten<b>0</b></li></ul>
  <p class="packet__label">Dietary Supplement</p>
</article>

<article class="packet packet--small packet--summit">
  <svg class="packet__ground" viewBox="0 0 320 506" preserveAspectRatio="none" aria-hidden="true">
    <path class="packet__panel" d="M0 118 C90 55 210 40 320 48 L320 402 C220 428 110 455 0 478 Z"/>
    <path class="packet__swoosh" d="M0 486 C110 462 220 436 320 410"/>
  </svg>
  <p class="packet__trust">Trusted for over<span class="packet__trust-years">25 <small>years</small></span>Original</p>
  <p class="packet__tagline">FAST<span class="packet__tagline-star">★</span>BALANCED<span class="packet__tagline-star">★</span>LASTING</p>
  <div class="packet__brand"><span class="packet__brand-name">BRISKLO</span><span class="packet__brand-dot"></span></div>
  <p class="packet__est">EST.1985</p>
  <div class="packet__formula">
    <p class="packet__ingredients">5-HTP-CoQ10-ROYAL JELLY</p>
    <h2 class="packet__name">SUMMIT MIX</h2>
    <p class="packet__extras">VITAMINS, MINERALS<br>ELEUTHERO, CAYENNE<br>SCISANDRA</p>
  </div>
  <p class="packet__count">USA<br>3 TABLETS</p>
  <ul class="packet__facts"><li class="packet__fact">Calories<b>0</b></li><li class="packet__fact">Sugar<b>0</b></li><li class="packet__fact">Gluten<b>0</b></li></ul>
  <p class="packet__label">Dietary Supplement</p>
</article>

</body>
</html>
```